App Design Project

We are building an app and looking for design help on an existing template. We will also need a style guide. For more information, there is a website which outlines the assignment with visuals. Go here:

http://www.brivolane.com/

Industry/Entity Type

Building

```html
<!DOCTYPE html>
<html lang="en">
<head>
<meta charset="utf-8">
<title>Activities</title>
<link rel="stylesheet" href="https://fonts.googleapis.com/css2?family=Oswald:wght@400;500&family=Arimo:wght@400&display=swap">
<style>
  :root {
    --screen-bg: #1b1c1d;
    --header-bg: #0f1315;
    --card-bg: #2d2e2f;
    --card-edge: #3c3d3e;
    --coral-light: #e9876a;
    --coral-dark: #a9432f;
    --coral-edge: #6e2a1d;
    --crimson-light: #b8304f;
    --crimson-dark: #7d1429;
    --green-light: #6fdc8a;
    --green-dark: #1f8a3d;
    --title-green: #6ff09a;
    --detail-green: #82f08c;
    --expire-green: #3fbf4c;
    --dark-text: #1a1412;
    --pale-text: #f2e6e6;
    --name-orange: #f0a030;
  }
  html, body {
    margin: 0;
    width: 710px;
    height: 1200px;
    overflow: hidden;
    background: var(--screen-bg);
  }
  .screen {
    position: relative;
    width: 710px;
    height: 1200px;
    background: var(--screen-bg);
    font-family: "Oswald", sans-serif;
  }
  .top-bar {
    position: absolute;
    left: 0; top: 0;
    width: 710px; height: 212px;
    background: var(--header-bg);
  }
  .round-btn, .tab-btn, .filter-pill, .title-pill {
    position: absolute;
    display: flex;
    align-items: center;
    justify-content: center;
    box-sizing: border-box;
    text-transform: uppercase;
  }
  .round-btn {
    top: 32px;
    width: 146px; height: 146px;
    border-radius: 50%;
    background: radial-gradient(circle at 45% 35%, var(--coral-light), var(--coral-dark));
    border: 3px solid var(--coral-edge);
    color: var(--dark-text);
    font-size: 40px;
    font-weight: 500;
  }
  .round-btn.back { left: 9px; }
  .round-btn.sort { left: 560px; }
  .title-pill {
    left: 182px; top: 44px;
    width: 351px; height: 118px;
    border-radius: 34px;
    background: linear-gradient(var(--green-light), var(--green-dark));
    border: 3px solid #145a27;
    color: var(--dark-text);
    font-size: 42px;
    font-weight: 500;
  }
  .filter-pill {
    top: 256px;
    width: 204px; height: 72px;
    border-radius: 36px;
    background: linear-gradient(var(--crimson-light), var(--crimson-dark));
    border: 2px solid #4d0a18;
    color: var(--pale-text);
    font-size: 28px;
  }
  .activity-card {
    position: absolute;
    left: 0; top: 406px;
    width: 710px; height: 326px;
    background: var(--card-bg);
    border-top: 2px solid var(--card-edge);
    border-bottom: 2px solid var(--card-edge);
    box-sizing: border-box;
  }
  .activity-title {
    position: absolute;
    left: 20px; top: 14px;
    margin: 0;
    color: var(--title-green);
    font-size: 66px;
    font-weight: 400;
    line-height: 1.2;
    letter-spacing: 1px;
  }
  .activity-detail {
    position: absolute;
    left: 22px;
    margin: 0;
    color: var(--detail-green);
    font-size: 34px;
    line-height: 1;
  }
  .activity-detail.venue { top: 108px; }
  .activity-detail.date { top: 166px; }
  .activity-expiry {
    position: absolute;
    left: 22px; top: 232px;
    margin: 0;
    color: var(--expire-green);
    font-size: 32px;
    line-height: 1;
  }
  .host-photo {
    position: absolute;
    left: 526px; top: 116px;
    width: 128px; height: 136px;
    border-radius: 6px;
    background: radial-gradient(circle at 50% 40%, #e27f62, #a4402c);
    border: 3px solid var(--coral-edge);
    box-sizing: border-box;
  }
  .host-name {
    position: absolute;
    left: 510px; top: 262px;
    width: 160px;
    text-align: center;
    font-family: "Arimo", sans-serif;
    font-size: 25px;
    color: var(--name-orange);
  }
  .open-arrow {
    position: absolute;
    left: 664px; top: 160px;
  }
  .tab-btn {
    top: 1041px;
    width: 126px; height: 130px;
    border-radius: 8px;
    background: radial-gradient(circle at 50% 40%, var(--coral-light), var(--coral-dark));
    border: 3px solid var(--coral-edge);
    color: var(--dark-text);
    font-size: 32px;
    line-height: 1;
    text-align: center;
  }
</style>
</head>
<body>
<main class="screen">
  <header class="top-bar">
    <div class="round-btn back">Back</div>
    <div class="title-pill">Activities</div>
    <div class="round-btn sort">Sort</div>
  </header>

  <nav>
    <div class="filter-pill" style="left:22px">Search All</div>
    <div class="filter-pill" style="left:251px">People</div>
    <div class="filter-pill" style="left:480px">Groups</div>
  </nav>

  <article class="activity-card">
    <h2 class="activity-title">MIDNIGHT MONSTER SHOW</h2>
    <p class="activity-detail venue">OLD TOWN CINEMA</p>
    <p class="activity-detail date">OCTOBER 8, 2012, 12.00AM</p>
    <p class="activity-expiry">Expires in 6hrs, 39 mins</p>
    <div class="host-photo" role="img" aria-label="Profile picture of the host member"></div>
    <div class="host-name">NANCY 14</div>
    <svg class="open-arrow" width="24" height="40" viewBox="0 0 24 40" aria-hidden="true">
      <polyline points="5,6 18,20 5,34" fill="none" stroke="#f07a20" stroke-width="5"/>
    </svg>
  </article>

  <footer>
    <div class="tab-btn" style="left:18px">Search</div>
    <div class="tab-btn" style="left:155px">New<br>Posts</div>
    <div class="tab-btn" style="left:295px">Msgs</div>
    <div class="tab-btn" style="left:433px">Alerts</div>
    <div class="tab-btn" style="left:571px">More</div>
  </footer>
</main>
</body>
</html>
```